Small Artisan Bakery Needs a new Bread Bag Label

I'm looking for a new bread bag label design for our artisan bakery. I have attached photos of our current logo (we will be using this in the label) and pictures of our bread bag. For this project we will focus on one of our bread (100% Rye) however I would like the final final to be in a format I can edit for other bread types.

We are thinking that each bread bag will have 2 labels, our logo on top of the bread bag window (as shown in the attached photos) and simple bread description below the window.

We typically use Copperplate font however we are open to ideas as long as it keeps in alignment with our logo.

*Also note, we will not be printing the labels directly on the bag. The designs will be printed as labels that will be stuck on each bag. I would like to have the final designs formatted in a way that makes it simple to have printed at a standard printing shop.

The bag is 9.5" long, 5" wide.

The length fro the bottom of the bag window to the bottom of the bag is 2".

Top of the bag to top of the window is a little over 4".

Since these labels will be printed on label paper and manually stuck on the bag I would like them to not be take up up the whole space above or below the bag window. If the label design comes to the edge of the bag it will be very difficult to physically stick the label on the bag straight.

Thanks

Hi, The bag is 9.5" long, 5" wide. The length fro the bottom of the bag window to the bottom of the bag is 2". Top of the bag to top of the window is a little over 4". Since these labels will be printed on label paper and manually stuck on the bag I would like them to not be take up up the whole space above or below the bag window. If the label design comes to the edge of the bag it will be very difficult to physically stick the label on the bag straight. Thanks

```html
<!DOCTYPE html>
<html lang="en">
<head>
<meta charset="utf-8">
<title>Willow Brook Bread – Bag Labels</title>
<link rel="stylesheet" href="https://fonts.googleapis.com/css2?family=Cinzel:wght@400;600&family=Arimo:wght@400&display=swap">
<style>
  :root {
    --bag-brown: #774b1f;
    --label-paper: #fdfcf8;
    --ink-brown: #7a4e22;
    --ink-dark: #4b3a2c;
    --rule-brown: #8a6038;
    --dim-white: #ffffff;
  }
  * { margin: 0; padding: 0; box-sizing: border-box; }
  html, body { width: 1200px; height: 2278px; overflow: hidden; }
  body {
    position: relative;
    background: var(--bag-brown);
    font-family: "Cinzel", "Times New Roman", serif;
  }
  .label {
    position: absolute;
    left: 146px;
    width: 912px;
    background: var(--label-paper);
  }
  .label::after {
    content: "";
    position: absolute;
    inset: 11px;
    border: 2px solid var(--rule-brown);
    pointer-events: none;
  }
  .label--logo { top: 114px; height: 932px; }
  .label--description { top: 1686px; height: 461px; }

  .centered { position: absolute; left: 0; right: 0; text-align: center; }

  .brand-name {
    top: 300px;
    font-size: 96px;
    line-height: 1.15;
    font-weight: 600;
    color: var(--ink-brown);
    letter-spacing: 3px;
  }
  .since { top: 600px; font-size: 44px; color: var(--ink-brown); letter-spacing: 2px; }
  .globe-icon { position: absolute; top: 676px; left: 439px; }
  .web-address { top: 730px; font-size: 27px; color: var(--ink-dark); letter-spacing: 1.5px; }
  .divider {
    position: absolute; top: 780px; left: 181px; width: 550px;
    height: 2px; background: var(--rule-brown);
  }
  .social-dot {
    position: absolute; top: 810px; left: 445px; width: 22px; height: 22px;
    border-radius: 50%; background: var(--ink-brown);
  }
  .social-address { top: 858px; font-size: 26px; color: var(--ink-dark); letter-spacing: 1px; }

  .bread-title { top: 40px; font-size: 76px; color: var(--ink-dark); letter-spacing: 1px; }
  .bread-subtitle { top: 170px; font-size: 20px; color: var(--ink-dark); letter-spacing: 0.5px; }
  .brand-name--small {
    top: 250px; font-size: 34px; font-weight: 600;
    color: var(--ink-brown); letter-spacing: 2px;
  }
  .ingredients {
    position: absolute; top: 362px; left: 44px;
    display: flex; align-items: center; gap: 10px; color: var(--ink-dark);
  }
  .ingredients__percent { font-size: 57px; line-height: 1; }
  .ingredients__list { font-size: 23px; line-height: 1.3; letter-spacing: 0.5px; }

  .dimension {
    position: absolute;
    font-family: "Arimo", Arial, sans-serif;
    font-size: 50px;
    color: var(--dim-white);
  }
  .dimension--vertical { transform: translate(-50%, -50%) rotate(-90deg); }
  .dimension--horizontal { transform: translateX(-50%); }
</style>
</head>
<body>
  <section class="label label--logo">
    <div class="centered brand-name">Willow Brook<br>Bread</div>
    <div class="centered since">Since: 1921</div>
    <svg class="globe-icon" width="34" height="34" viewBox="0 0 34 34" aria-hidden="true"
         fill="none" stroke="#7a4e22" stroke-width="2">
      <circle cx="17" cy="17" r="15"/>
      <ellipse cx="17" cy="17" rx="7" ry="15"/>
      <line x1="2" y1="17" x2="32" y2="17"/>
      <path d="M5 9h24M5 25h24"/>
    </svg>
    <div class="centered web-address">www.willowbrookbread.com</div>
    <div class="divider"></div>
    <div class="social-dot"></div>
    <div class="centered social-address">https://social.example/WillowBrookBread</div>
  </section>

  <section class="label label--description">
    <div class="centered bread-title">100% Rye Bread</div>
    <div class="centered bread-subtitle">naturally leavened and fermented 100% Lithuanian rye bread.</div>
    <div class="centered brand-name--small">Willow Brook Bread</div>
    <div class="ingredients">
      <span class="ingredients__percent">100%</span>
      <span class="ingredients__list">organic rye flour, 110 year old organic<br>rye culture, and grey Celtic sea salt</span>
    </div>
  </section>

  <span class="dimension dimension--vertical" style="left:72px; top:551px;">3.9”</span>
  <span class="dimension dimension--horizontal" style="left:602px; top:1070px;">3.8”</span>
  <span class="dimension dimension--vertical" style="left:72px; top:1918px;">1.9”</span>
  <span class="dimension dimension--horizontal" style="left:602px; top:2180px;">3.8”</span>
</body>
</html>
```